PowerPoint Template Needed for Investment Firm

Norvelle Capital Management is an emerging wealth management firm based in New Jersey. It offers superior investment returns to high net worth individuals and institutions by finding undervalued assets.

We recently selected a company logo which was inspired by the Norvelle constellation. Beta Tucanae is a group of six stars, containing star cluster 47 Tucanae, rated the second brightest object in the sky.

Now we need a PowerPoint template with the designs for the following:

1. Title/cover page slide
2. Content slide with title
3. Section slide - to introduce a new section
4. Final slide - with contact information

The slides will be used at investor presentations, that is, to provide information about the company to potential investors. Since we are an investment firm, the design should project a sense of stability, growth and professionalism. The owner is interested in something simple yet striking, which of course is consistent with the logo. I'm thinking more conservative colors and Sans Serif fonts.

I plan on changing the status to non-refundable once I see some designs that I really like.

Target Market(s)

Wealthy individuals, probably middle aged or older, in the US

Industry/Entity Type

Conservative

Requirements
Must have
• Sans serif fonts
Clean, very professional look
Conservative colors that complement existing logo
Should not have
• Anything too busy or complicated

```html
<!DOCTYPE html>
<html lang="en">
<head>
<meta charset="utf-8">
<title>Norvelle Capital Management – Content Slide</title>
<link href="https://fonts.googleapis.com/css2?family=Open+Sans:wght@400;600;700&display=swap" rel="stylesheet">
<style>
  :root {
    --brand-blue: #0b2a94;
    --brand-blue-deep: #07207a;
    --rule-grey: #9a9ca3;
    --text-grey: #545860;
    --bullet-blue: #3a3fb0;
    --bg-light: #ffffff;
    --bg-mid: #eceef2;
    --bg-low: #dfe3ec;
    --white: #ffffff;
  }
  * { margin: 0; padding: 0; box-sizing: border-box; }
  html, body { width: 1200px; height: 900px; overflow: hidden; }
  body { font-family: "Open Sans", Arial, sans-serif; background: var(--bg-light); }

  .slide {
    position: relative;
    width: 1200px;
    height: 900px;
    overflow: hidden;
    background: linear-gradient(180deg, var(--bg-light) 0%, var(--bg-mid) 55%, var(--bg-low) 100%);
  }
  .slide-texture {
    position: absolute;
    right: 0; top: 60px;
    width: 760px; height: 720px;
    background: radial-gradient(ellipse at 75% 45%, rgba(190,194,204,0.45) 0%, rgba(210,213,220,0.2) 45%, rgba(255,255,255,0) 70%);
  }
  .header-band { position: absolute; left: 0; top: 0; width: 1200px; height: 160px; }
  .slide-title {
    position: absolute;
    left: 34px; top: 46px;
    font-weight: 700;
    font-size: 39px;
    letter-spacing: 0.3px;
    color: var(--white);
  }
  .intro {
    position: absolute;
    left: 50px; top: 231px;
    width: 1100px;
    font-size: 21.5px;
    line-height: 45px;
    color: var(--text-grey);
  }
  .key-points {
    position: absolute;
    left: 58px; top: 376px;
    list-style: none;
  }
  .key-points li {
    font-size: 28.5px;
    line-height: 61.5px;
    color: var(--text-grey);
    white-space: nowrap;
  }
  .key-points li::before {
    content: "»";
    color: var(--bullet-blue);
    font-size: 24px;
    margin-right: 14px;
    position: relative;
    top: -4px;
  }
  .footer-band {
    position: absolute;
    left: 0; bottom: 0;
    width: 1200px; height: 51px;
    background: var(--brand-blue);
  }
  .brand-mark {
    position: absolute;
    left: 34px; top: 815px;
    width: 76px; height: 76px;
    background: var(--brand-blue-deep);
    border: 2px solid #8f9bd6;
    border-radius: 7px;
  }
  .brand-name {
    position: absolute;
    left: 124px; top: 857px;
    font-size: 21px;
    font-weight: 600;
    letter-spacing: 4px;
    color: var(--white);
  }
</style>
</head>
<body>
  <main class="slide">
    <div class="slide-texture" role="img" aria-label="Soft grey dot texture fading across the right side"></div>

    <svg class="header-band" viewBox="0 0 1200 160" aria-hidden="true">
      <path d="M0 0 H1200 V95 C1060 72 900 60 750 67 C500 80 260 150 0 140 Z" fill="var(--brand-blue)"/>
      <path d="M0 140 C260 150 500 80 750 67 C900 60 1060 72 1200 95" fill="none" stroke="var(--rule-grey)" stroke-width="5"/>
    </svg>
    <h1 class="slide-title">INSERT TITLE HERE</h1>

    <p class="intro">Lorem ipsum dolor sit Lorem ipsum dolor sit Lorem ipsum dolor sit Lorem ipsum dolor sit-<br>Lorem ipsum dolor sit Lorem ipsum dolor sitLorem ipsum dolor sit Lorem ipsum dolor sit</p>

    <ul class="key-points">
      <li>Lorem ipsum dolor sit ipsum Lorem ipsum dolor sit ipsum</li>
      <li>Lorem ipsum dolor sit ipsum Lorem ipsum dolor sit ipsum</li>
      <li>Lorem ipsum dolor sit ipsum Lorem ipsum dolor sit ipsum</li>
      <li>Lorem ipsum dolor sit ipsum Lorem ipsum dolor sit ipsum</li>
      <li>Lorem ipsum dolor sit ipsum Lorem ipsum dolor sit ipsum</li>
    </ul>

    <footer class="footer-band"></footer>
    <div class="brand-mark"></div>
    <div class="brand-name">NORVELLE</div>
  </main>
</body>
</html>
```